Gutschein-Design für Friseursalon gesucht
Zielgruppe
Wir sind ein Friseursalon für Jung bis Alt.
Wir bieten alles rund um das Haar an und verkaufen Haarpflegeprodukte.
Aufgabenstellung
Das Design sollte Modern und Professionell wirken.
Ebenso muss es zu unserem Firmenlogo passen.
Es sollte auf die Rückseite des Gutscheins ein Feld für den Betrag, für Wen, das Datum, den Stempel und die Gutscheinnummer vorhanden sein.

```html
<!DOCTYPE html>
<html lang="de">
<head>
<meta charset="utf-8">
<title>Gutschein – Lockenstudio Veri</title>
<link href="https://fonts.googleapis.com/css2?family=Mr+Dafoe&family=Roboto+Condensed:wght@300;400&display=swap" rel="stylesheet">
<style>
  :root{
    --slate:#353a3d;
    --plum:#8a2a87;
    --mist:#d9d9d9;
    --white:#ffffff;
    --paper:#ffffff;
    --photo-light:#f1edf0;
    --photo-mid:#d6d1d5;
    --photo-deep:#a9a4a8;
  }
  *{margin:0;padding:0;box-sizing:border-box}
  html,body{width:1200px;height:2369px;overflow:hidden;background:var(--paper)}
  body{position:relative;font-family:"Roboto Condensed",Arial,sans-serif}
  .card{position:absolute;overflow:hidden}
  .card svg.shapes{position:absolute;left:0;top:0}
  .front{left:0;top:0;width:1147px;height:1147px}
  .back{left:9px;top:1211px;width:1148px;height:1150px}
  .script{font-family:"Mr Dafoe",cursive;color:var(--white);position:absolute;white-space:nowrap;line-height:1}
  .front-title{font-size:145px;left:140px;top:570px;transform:translate(-50%,-50%) rotate(-90deg)}
  .back-title{font-size:120px;left:62px;top:82px}
  .brand{position:absolute;font-weight:400;color:var(--slate);white-space:nowrap;display:flex;align-items:center;gap:12px}
  .brand .dot{width:16px;height:16px;border-radius:50%;background:var(--slate)}
  .front-brand{left:790px;top:1010px;font-size:40px}
  .back-brand{left:725px;top:960px;font-size:50px}
  .field-label{position:absolute;color:var(--white);font-weight:300;font-size:26px;text-align:right;white-space:nowrap}
  .label-amount{right:658px;top:240px}
  .label-for{right:731px;top:495px}
  .label-date{right:700px;top:750px}
  .owner{position:absolute;left:73px;top:835px;color:var(--white);font-weight:300}
  .owner .name{font-size:31px;line-height:36px}
  .owner .role{font-size:24px;line-height:30px}
  .address{position:absolute;left:68px;top:935px;color:var(--white);font-weight:300;font-size:26px;line-height:32px}
  .voucher-no{position:absolute;left:73px;top:1084px;font-size:24px;color:#222}
</style>
</head>
<body>

<section class="card front">
  <svg class="shapes" width="1147" height="1147" viewBox="0 0 1147 1147">
    <defs>
      <linearGradient id="frontPhotoTone" x1="0" y1="0" x2="1" y2="1">
        <stop offset="0" stop-color="var(--photo-mid)"/>
        <stop offset="0.5" stop-color="var(--photo-light)"/>
        <stop offset="1" stop-color="var(--photo-deep)"/>
      </linearGradient>
    </defs>
    <rect width="1147" height="1147" fill="var(--slate)"/>
    <g role="img" aria-label="Porträtfoto einer blonden Frau mit lockigem Haar und violettem Make-up">
      <rect x="707" y="0" width="440" height="1147" fill="url(#frontPhotoTone)"/>
      <circle cx="694" cy="568" r="452" fill="url(#frontPhotoTone)"/>
    </g>
  </svg>
  <div class="script front-title">Gutschein</div>
  <div class="brand front-brand"><span class="dot"></span>Lockenstudio Veri</div>
</section>

<section class="card back">
  <svg class="shapes" width="1148" height="1150" viewBox="0 0 1148 1150">
    <defs>
      <linearGradient id="backPhotoTone" x1="0" y1="0" x2="1" y2="1">
        <stop offset="0" stop-color="var(--photo-light)"/>
        <stop offset="0.55" stop-color="var(--photo-mid)"/>
        <stop offset="1" stop-color="var(--photo-light)"/>
      </linearGradient>
    </defs>
    <rect width="1148" height="1150" fill="var(--slate)"/>
    <rect class="contact-band" x="0" y="807" width="900" height="257" fill="var(--plum)"/>
    <rect class="number-band" x="0" y="1064" width="900" height="56" fill="var(--mist)"/>
    <circle role="img" aria-label="Porträtfoto einer blonden Frau, Gesicht halb im Bild" cx="1057" cy="574" r="620" fill="url(#backPhotoTone)"/>
    <g class="entry-fields" fill="var(--white)">
      <rect x="520" y="268" width="628" height="24" opacity="0.35"/>
      <rect x="444" y="524" width="704" height="24" opacity="0.35"/>
      <rect x="472" y="780" width="676" height="4" opacity="0.45"/>
    </g>
  </svg>
  <div class="script back-title">Gutschein</div>
  <div class="field-label label-amount">Betrag</div>
  <div class="field-label label-for">Gutschein für</div>
  <div class="field-label label-date">Datum / Stempel</div>
  <div class="owner">
    <div class="name">Veronika Sandhaus</div>
    <div class="role">Inhaberin Friseurmeisterin</div>
  </div>
  <div class="address">Lindenweg 8<br>54320 Mühlbach<br>Telefon: 06571/4820</div>
  <div class="voucher-no">Gutschein-Nr.</div>
  <div class="brand back-brand"><span class="dot"></span>Lockenstudio Veri</div>
</section>

</body>
</html>
```